Sticker Design for Company Equipment - Velunora

We are looking for a professional and clean graphic design for a set of stickers to apply on our company equipment (cleaning, gardening, pest control). The stickers must include our logo (the square with the three colored segments and the checkmark), our phone number, email address, and website, you can decide to use all three or just our website based on your graphic needs. It is important that it has an attractive sharp and clear look. The design should be consistent with our brand identity and give a polished, trustworthy look to our tools and machinery. We need a modular design that works in different formats (rectangular, square, round), depending on the type of equipment.

Need extra days to review

```html
<!DOCTYPE html>
<html lang="en">
<head>
<meta charset="utf-8">
<title>Velunora Sticker Design</title>
<link href="https://fonts.googleapis.com/css2?family=Montserrat:wght@400;500;600;700&family=Oswald:wght@300;500;700&display=swap" rel="stylesheet">
<style>
  :root{
    --navy:#27235f;
    --green:#6dbb45;
    --orange:#e8622a;
    --paper:#ffffff;
    --surface:#d4d4d6;
    --header-dark:#4a4a4c;
    --header-light:#9a9a9d;
    --header-text:#dcdcdc;
    --label:#8a8a8c;
  }
  *{margin:0;padding:0;box-sizing:border-box}
  html,body{width:1200px;height:855px;overflow:hidden;background:var(--paper);font-family:"Montserrat",sans-serif}
  .presentation{position:relative;width:1200px;height:855px}
  .preview-panel{position:absolute;left:0;top:0;width:736px;height:855px;background:var(--surface)}
  .brief-header{position:absolute;left:0;top:0;width:736px;height:143px;
    background:linear-gradient(90deg,var(--header-dark),var(--header-light));color:var(--header-text);padding:14px 0 0 40px}
  .brief-title{font-size:36px;font-weight:500;line-height:46px;letter-spacing:.3px}
  .brief-line{font-size:24px;font-weight:500;line-height:40px}
  .hero-sticker{position:absolute;left:163px;top:295px;width:410px;height:410px}
  .options-column{position:absolute;left:849px;top:0;width:240px;height:855px}
  .option{position:absolute;left:0;width:240px;text-align:center}
  .option-label{font-size:15px;font-weight:500;color:var(--label);height:22px;line-height:22px}
  .option svg{display:block;width:232px;height:232px;margin:6px auto 0}
  .option-1{top:19px}.option-2{top:290px}.option-3{top:560px}
  .ring-text{font-family:"Montserrat",sans-serif;font-weight:600;fill:var(--paper);font-size:12.5px}
  .ring-text.condensed{font-family:"Oswald",sans-serif;font-weight:700;font-size:13.5px}
  .top-web{font-family:"Montserrat",sans-serif;font-weight:500;fill:var(--green);font-size:12.5px;letter-spacing:1px}
  .top-web.condensed{font-family:"Oswald",sans-serif;font-weight:300;font-size:13px}
  .top-phone{font-family:"Montserrat",sans-serif;font-weight:700;fill:var(--paper);font-size:17px;letter-spacing:1px}
  .brand-name{font-family:"Montserrat",sans-serif;font-weight:700;fill:var(--navy);font-size:21px}
  .contact{font-family:"Montserrat",sans-serif;font-weight:700;fill:var(--navy);font-size:11.5px}
  .contact.small{font-size:9px}
  .contact.condensed{font-family:"Oswald",sans-serif;font-weight:500;font-size:13.5px}
  .dot{fill:var(--orange)}
</style>
</head>
<body>
<svg width="0" height="0" style="position:absolute" aria-hidden="true">
  <defs>
    <path id="arc-top" d="M -88,0 A 88 88 0 0 1 88,0"/>
    <path id="arc-bottom" d="M -101,0 A 101 101 0 0 0 101,0"/>
    <radialGradient id="center-glow" cx="50%" cy="50%" r="55%">
      <stop offset="0" stop-color="#ffffff"/>
      <stop offset=".55" stop-color="#f3f2f0"/>
      <stop offset=".8" stop-color="#f6e3d2"/>
      <stop offset="1" stop-color="#e3eedc"/>
    </radialGradient>
    <g id="sticker-base">
      <circle r="113" fill="var(--navy)" stroke="var(--green)" stroke-width="3"/>
      <circle r="79" fill="none" stroke="var(--orange)" stroke-width="1.6"/>
      <circle r="76" fill="url(#center-glow)" role="img" aria-label="Soft swirl of light orange and green behind the brand name"/>
    </g>
    <path id="phone-icon" d="M3 1h3l1.5 3.5-2 1.2a8 8 0 0 0 3.8 3.8l1.2-2L14 9v3a1.5 1.5 0 0 1-1.6 1.5A12.5 12.5 0 0 1 1.5 2.6 1.5 1.5 0 0 1 3 1z"/>
  </defs>
</svg>

<main class="presentation">
  <section class="preview-panel">
    <svg class="hero-sticker" viewBox="-120 -120 240 240" role="img" aria-label="Round sticker, version 2">
      <circle r="119" fill="var(--paper)"/>
      <use href="#sticker-base"/>
      <text class="top-web"><textPath href="#arc-top" startOffset="50%" text-anchor="middle">www.velunora.srl</textPath></text>
      <text class="ring-text"><textPath href="#arc-bottom" startOffset="50%" text-anchor="middle" textLength="292" lengthAdjust="spacing">CLEANING <tspan class="dot">•</tspan> GARDENING <tspan class="dot">•</tspan> PESTCONTROL</textPath></text>
      <rect x="-58" y="-13" width="11" height="11" fill="var(--green)"/>
      <text class="brand-name" x="-41" y="-1">Velunora</text>
      <use href="#phone-icon" x="-48" y="12" fill="var(--navy)" transform="translate(-2 1) scale(1)"/>
      <text class="contact" x="-30" y="24">328 555 0147</text>
    </svg>
  </section>

  <header class="brief-header">
    <h1 class="brief-title">Velunora Sticker Design</h1>
    <p class="brief-line">Size of Round Sticker: 5” x 5”</p>
    <p class="brief-line">This size can be reduce in any required size</p>
  </header>

  <section class="options-column">
    <div class="option option-1">
      <p class="option-label">Option-1</p>
      <svg viewBox="-120 -120 240 240" role="img" aria-label="Round sticker, option 1">
        <use href="#sticker-base"/>
        <text class="top-phone"><textPath href="#arc-top" startOffset="50%" text-anchor="middle">328 555 0147</textPath></text>
        <text class="ring-text"><textPath href="#arc-bottom" startOffset="50%" text-anchor="middle" textLength="300" lengthAdjust="spacing">CLEANING <tspan class="dot">•</tspan> GARDENING <tspan class="dot">•</tspan> PESTCONTROL</textPath></text>
        <rect x="-58" y="-13" width="11" height="11" fill="var(--green)"/>
        <text class="brand-name" x="-41" y="-1">Velunora</text>
        <text class="contact small" x="0" y="20" text-anchor="middle">www.velunora.srl</text>
      </svg>
    </div>

    <div class="option option-2">
      <p class="option-label">Option-2</p>
      <svg viewBox="-120 -120 240 240" role="img" aria-label="Round sticker, option 2">
        <use href="#sticker-base"/>
        <text class="top-web"><textPath href="#arc-top" startOffset="50%" text-anchor="middle">www.velunora.srl</textPath></text>
        <text class="ring-text"><textPath href="#arc-bottom" startOffset="50%" text-anchor="middle" textLength="300" lengthAdjust="spacing">CLEANING <tspan class="dot">•</tspan> GARDENING <tspan class="dot">•</tspan> PESTCONTROL</textPath></text>
        <rect x="-58" y="-13" width="11" height="11" fill="var(--green)"/>
        <text class="brand-name" x="-41" y="-1">Velunora</text>
        <use href="#phone-icon" x="-50" y="13" fill="var(--navy)"/>
        <text class="contact" x="-32" y="24">328 555 0147</text>
      </svg>
    </div>

    <div class="option option-3">
      <p class="option-label">Option-3</p>
      <svg viewBox="-120 -120 240 240" role="img" aria-label="Round sticker, option 3">
        <use href="#sticker-base"/>
        <text class="top-web condensed"><textPath href="#arc-top" startOffset="50%" text-anchor="middle">www.velunora.srl</textPath></text>
        <text class="ring-text condensed"><textPath href="#arc-bottom" startOffset="50%" text-anchor="middle" textLength="300" lengthAdjust="spacing">CLEANING <tspan class="dot">•</tspan> GARDENING <tspan class="dot">•</tspan> PESTCONTROL</textPath></text>
        <rect x="-58" y="-13" width="11" height="11" fill="var(--green)"/>
        <text class="brand-name" x="-41" y="-1">Velunora</text>
        <use href="#phone-icon" x="-46" y="12" fill="var(--navy)"/>
        <text class="contact condensed" x="-28" y="25">328 555 0147</text>
      </svg>
    </div>
  </section>
</main>
</body>
</html>
```